Catering Menu

We are looking at revamping our catering menu to appeal to the corporate and home catering Market.
Attached is our current menu. These items are current, and are required on the new design.
Pictures to be added of platters of what we offer
we are a upmarket venue in Melbourne Australia
we are looking to offer an off site catering option for our clients.
we are aiming to appeal to home celebrations, office and corporate functions.
The menu must pop, and catch the eye of the customer.
this will be done in a mail drop also.
6 sided DL flyer.

Target Market(s)

General Catering for businesses & people at home

Industry/Entity Type

Restaurant

Requirements
Must have
• Pictures of catering food, clear lay out of menu and pricing

```html
<!DOCTYPE html>
<html lang="en">
<head>
<meta charset="utf-8">
<title>Catering Menu – DL Trifold</title>
<link rel="stylesheet" href="https://fonts.googleapis.com/css2?family=Great+Vibes&family=Lato:ital,wght@0,400;0,700;1,400&display=swap">
<style>
  :root{
    --backdrop:#e4e5e7;
    --paper:#ffffff;
    --sky:#cfe3f3;
    --sky-deep:#a9cbe6;
    --ink:#2b2b2b;
    --ink-soft:#5c6670;
    --accent:#c8323a;
    --food-warm:#b4643c;
    --food-dark:#5a3a2c;
    --food-green:#7c9a4a;
  }
  *{box-sizing:border-box;margin:0;padding:0}
  html,body{width:900px;height:1200px;overflow:hidden}
  body{background:var(--backdrop);font-family:"Lato",sans-serif;color:var(--ink);
       display:flex;flex-direction:column;align-items:center;justify-content:center;gap:30px}
  .sheet{width:840px;height:560px;display:flex;background:var(--paper);
         box-shadow:0 6px 18px rgba(0,0,0,.18)}
  .panel{width:280px;height:100%;position:relative;overflow:hidden}
  .panel + .panel{border-left:1px solid #e6edf3}

  .menu-panel{background:linear-gradient(180deg,var(--sky) 0%,#eef5fb 40%,#f7fafd 70%,var(--sky) 100%);
              padding:34px 26px}
  .menu-panel .photo-fade{position:absolute;left:0;right:0;height:110px}
  .photo-fade.top{top:0;background:linear-gradient(180deg,rgba(180,100,60,.35),rgba(255,255,255,0))}
  .photo-fade.bottom{bottom:0;background:linear-gradient(0deg,rgba(124,154,74,.35),rgba(255,255,255,0))}
  .menu-body{position:relative;background:rgba(255,255,255,.72);padding:18px 16px;height:100%}
  .section-title{font-family:"Great Vibes",cursive;color:var(--accent);font-size:26px;
                 text-align:center;margin:4px 0 8px}
  .section-title + .menu-list{margin-bottom:14px}
  .menu-list{list-style:none}
  .menu-list li{display:flex;justify-content:space-between;font-size:10.5px;padding:5px 0;
                border-bottom:1px dotted #b9c6d2}
  .menu-list .price{font-weight:700;color:var(--ink-soft)}

  .hero-panel{background:radial-gradient(ellipse at 60% 55%,var(--food-warm) 0%,var(--food-dark) 55%,#3a2a22 100%)}
  .hero-panel .photo{position:absolute;inset:0}
  .address-disc{position:absolute;left:-30px;top:170px;width:200px;height:200px;border-radius:50%;
                background:var(--paper);display:flex;flex-direction:column;justify-content:center;
                align-items:center;text-align:center;font-size:11px;line-height:1.5;padding-left:30px}
  .address-disc .venue{font-weight:700}

  .cover-panel{background:linear-gradient(180deg,#ffffff 0%,var(--sky) 100%);padding:30px 26px;
               display:flex;flex-direction:column;align-items:center}
  .cover-photo{width:150px;height:150px;border-radius:50%;border:5px solid var(--paper);
               box-shadow:0 2px 8px rgba(0,0,0,.2);
               background:radial-gradient(circle at 40% 40%,var(--food-green),var(--food-warm) 60%,var(--food-dark))}
  .cover-title{font-family:"Great Vibes",cursive;color:var(--accent);font-size:62px;line-height:.9;
               text-align:center;margin-top:36px}
  .cover-tagline{font-style:italic;color:var(--ink-soft);font-size:14px;text-align:center;
                 margin-top:20px;line-height:1.4}
  .contact{margin-top:auto;text-align:center;font-size:11px;line-height:1.6;color:var(--ink)}
  .contact .label{font-family:"Great Vibes",cursive;color:var(--accent);font-size:20px}
</style>
</head>
<body>

<section class="sheet outside">
  <div class="panel menu-panel">
    <div class="photo-fade top" role="img" aria-label="Faded photo of a grazing platter"></div>
    <div class="photo-fade bottom" role="img" aria-label="Faded photo of a salad platter"></div>
    <div class="menu-body">
      <h3 class="section-title">Grazing Boards</h3>
      <ul class="menu-list">
        <li><span>Antipasto Board</span><span class="price">$85</span></li>
        <li><span>Cheese Selection</span><span class="price">$75</span></li>
        <li><span>Fruit Platter</span><span class="price">$60</span></li>
        <li><span>Dips and Breads</span><span class="price">$45</span></li>
      </ul>
      <h3 class="section-title">Finger Food</h3>
      <ul class="menu-list">
        <li><span>Mini Quiche</span><span class="price">$48</span></li>
        <li><span>Arancini Balls</span><span class="price">$52</span></li>
        <li><span>Chicken Skewers</span><span class="price">$58</span></li>
        <li><span>Spring Rolls</span><span class="price">$42</span></li>
      </ul>
    </div>
  </div>

  <div class="panel hero-panel">
    <div class="photo" role="img" aria-label="Photo of a topped flatbread pizza on a board"></div>
    <div class="address-disc">
      <span class="venue">Harbourline Dining</span>
      <span>Pty Ltd</span>
      <br>
      <span>120 Collins Lane</span>
      <span>Melbourne VIC 3000</span>
    </div>
  </div>

  <div class="panel cover-panel">
    <div class="cover-photo" role="img" aria-label="Round photo of a plated dish with dipping sauce"></div>
    <h1 class="cover-title">Catering<br>Menu</h1>
    <p class="cover-tagline">Your guide to<br>our platter<br>options available</p>
    <div class="contact">
      <div class="label">Call us</div>
      <div>03 9000 1234</div>
      <div>events@harbourline.example</div>
    </div>
  </div>
</section>

<section class="sheet inside">
  <div class="panel menu-panel">
    <div class="photo-fade top" role="img" aria-label="Faded photo of sandwich platters"></div>
    <div class="photo-fade bottom" role="img" aria-label="Faded photo of hot food trays"></div>
    <div class="menu-body">
      <h3 class="section-title">Sandwiches &amp; Wraps</h3>
      <ul class="menu-list">
        <li><span>Gourmet Sandwiches</span><span class="price">$65</span></li>
        <li><span>Wrap Selection</span><span class="price">$68</span></li>
        <li><span>Mini Rolls</span><span class="price">$55</span></li>
        <li><span>Croissant Platter</span><span class="price">$70</span></li>
      </ul>
      <h3 class="section-title">Hot Food</h3>
      <ul class="menu-list">
        <li><span>Roast Beef Sliders</span><span class="price">$80</span></li>
        <li><span>Pasta Bake</span><span class="price">$72</span></li>
        <li><span>Lamb Kofta</span><span class="price">$78</span></li>
      </ul>
    </div>
  </div>

  <div class="panel menu-panel">
    <div class="photo-fade top" role="img" aria-label="Faded photo of fresh salads"></div>
    <div class="photo-fade bottom" role="img" aria-label="Faded photo of desserts"></div>
    <div class="menu-body">
      <h3 class="section-title">Salads</h3>
      <ul class="menu-list">
        <li><span>Caesar Salad</span><span class="price">$50</span></li>
        <li><span>Greek Salad</span><span class="price">$48</span></li>
        <li><span>Garden Salad</span><span class="price">$40</span></li>
        <li><span>Roast Pumpkin Salad</span><span class="price">$55</span></li>
      </ul>
      <h3 class="section-title">Sweets</h3>
      <ul class="menu-list">
        <li><span>Cake Selection</span><span class="price">$60</span></li>
        <li><span>Mini Tarts</span><span class="price">$54</span></li>
        <li><span>Brownie Platter</span><span class="price">$50</span></li>
      </ul>
    </div>
  </div>

  <div class="panel menu-panel">
    <div class="photo-fade top" role="img" aria-label="Faded photo of a breakfast spread"></div>
    <div class="photo-fade bottom" role="img" aria-label="Faded photo of drinks"></div>
    <div class="menu-body">
      <h3 class="section-title">Breakfast</h3>
      <ul class="menu-list">
        <li><span>Pastry Basket</span><span class="price">$45</span></li>
        <li><span>Yoghurt Cups</span><span class="price">$40</span></li>
        <li><span>Bacon Rolls</span><span class="price">$62</span></li>
      </ul>
      <h3 class="section-title">Drinks</h3>
      <ul class="menu-list">
        <li><span>Juice Jug</span><span class="price">$18</span></li>
        <li><span>Coffee Urn</span><span class="price">$35</span></li>
        <li><span>Soft Drinks</span><span class="price">$3</span></li>
      </ul>
    </div>
  </div>
</section>

</body>
</html>
```